Brochure Design

I would like to have this brochure design for a approval with the Tarovia chamber of commerce . It's a training program for people in Kenya Africa and the gov will pay for the training program. What ever you think would be better let me know. The letters in red are items that are free so I wanted that to stand out. I need to add the logo in the attachment added to the other logos on the front page.

Reason: I'm still looking for the right design and i'm looking to make a quick decision.

Industry/Entity Type

Chamber Of Commerce

```html
<!DOCTYPE html>
<html lang="en">
<head>
<meta charset="utf-8">
<title>Meridian Pathways Enterprises – Training Program Outline, pages 10–11</title>
<link rel="stylesheet" href="https://fonts.googleapis.com/css2?family=Arimo:wght@400;700&family=Open+Sans:wght@300;400&display=swap">
<style>
  :root {
    --backdrop: #4a4440;
    --paper: #ffffff;
    --ink: #1e1e1e;
    --orange: #f6a623;
    --orange-line: #f7c27a;
    --slate: #4a4d52;
    --panel: #b5b5b5;
    --spine: #d6d6d6;
    --white: #ffffff;
  }
  * { box-sizing: border-box; margin: 0; padding: 0; }
  html, body { width: 1200px; height: 900px; overflow: hidden; }
  body {
    background: var(--backdrop);
    font-family: "Arimo", Arial, sans-serif;
    color: var(--ink);
    position: relative;
  }
  .page {
    position: absolute;
    top: 52px;
    width: 563px;
    height: 800px;
    background: var(--paper);
  }
  .page--left { left: 38px; }
  .page--right {
    left: 600px;
    background: linear-gradient(90deg, var(--spine) 0px, #e4e4e4 40px, #f4f4f4 70px, var(--paper) 100px);
  }
  .abs { position: absolute; }

  /* photo placeholders */
  .photo { position: absolute; overflow: hidden; }
  .photo--garden {
    left: 0; top: 55px; width: 510px; height: 303px;
    border-top-right-radius: 22px;
    background: linear-gradient(180deg, #6b7d4a 0%, #8d8f78 30%, #6e8a3c 60%, #5c9a2a 80%, #4f8a22 100%);
  }
  .photo--fish {
    left: 52px; top: 379px; width: 511px; height: 171px;
    background: linear-gradient(160deg, #c8453a 0%, #e7dcd6 35%, #d9563f 55%, #eae6e3 75%, #3c4248 100%);
  }
  .photo__title {
    position: absolute;
    font-family: "Open Sans", Arial, sans-serif;
    font-weight: 300;
    color: var(--white);
    font-size: 20px;
    line-height: 20px;
    letter-spacing: 0.2px;
    text-shadow: 0 1px 2px rgba(0,0,0,.35);
  }
  .photo--garden .photo__title { right: 8px; bottom: 8px; text-align: right; }
  .photo--fish .photo__title { left: 14px; bottom: 6px; }

  .body-text { font-size: 11px; line-height: 14px; }
  .intro { left: 53px; top: 402px; width: 460px; }
  .intro p + p { margin-top: 6px; }

  .equipment-list { top: 486px; width: 224px; }
  .equipment-list--a { left: 53px; }
  .equipment-list--b { left: 288px; }
  .equipment-item { margin-bottom: 7px; }
  .equipment-item__name {
    font-weight: 700; font-size: 11px; line-height: 15px;
    padding-bottom: 2px;
    border-bottom: 2px solid var(--orange-line);
    margin-bottom: 5px;
  }

  .folio {
    position: absolute; top: 753px; height: 47px;
    font-size: 11px; display: flex; align-items: center;
  }
  .folio--left { left: 19px; }
  .folio--left .folio__rule { margin: 0 6px 0 8px; }
  .folio__rule { width: 2px; height: 47px; background: var(--orange); }
  .folio__label { font-size: 9px; letter-spacing: 0.2px; }
  .folio__label b { font-weight: 700; }
  .folio--right { left: 528px; }
  .folio--right .folio__rule { margin-right: 8px; }

  /* right page */
  .tab {
    position: absolute;
    font-family: "Arimo", Arial, sans-serif;
    font-weight: 700;
    font-size: 11px;
    line-height: 13px;
    padding: 2px 6px;
  }
  .tab--orange { background: var(--orange); color: var(--slate); border-top-right-radius: 10px; }
  .tab--skills { left: 52px; top: 54px; width: 156px; height: 17px; }
  .tab--equipment {
    left: 52px; top: 265px; width: 157px; height: 20px;
    background: var(--slate); color: var(--orange);
    font-family: "Open Sans", Arial, sans-serif; font-weight: 400; font-size: 16px; line-height: 16px;
  }
  .skill { position: absolute; left: 52px; width: 210px; }
  .skill__title {
    font-family: "Open Sans", Arial, sans-serif; font-weight: 300;
    font-size: 16px; line-height: 18px; letter-spacing: 0.3px;
    margin-bottom: 2px;
  }
  .skill--sprinklers { top: 80px; }
  .skill--design { top: 188px; }
  .equipment-note { left: 52px; top: 291px; width: 210px; }

  .info-panel {
    position: absolute; left: 270px; top: 50px; width: 293px; height: 306px;
    background: var(--panel);
    border-bottom-left-radius: 26px;
  }
  .info-panel__title {
    position: absolute; left: 22px; top: 31px;
    color: var(--white); font-weight: 700; font-size: 13px;
  }
  .info-panel__text { position: absolute; left: 25px; top: 49px; width: 218px; }
  .tab--dates { left: 25px; top: 141px; width: 146px; height: 23px; padding-top: 5px; }
  .tab--deposit { left: 25px; top: 261px; width: 146px; height: 25px; padding-top: 2px; line-height: 11px; }
  .info-bar {
    position: absolute; left: 25px; width: 215px; height: 19px;
    background: var(--slate); color: var(--orange-line);
    font-weight: 700; font-size: 11px; line-height: 19px; padding-left: 8px;
  }
  .info-bar--dates { top: 170px; }
  .info-bar--deposit { top: 293px; }

  .fish-col { top: 561px; width: 224px; }
  .fish-col--a { left: 52px; }
  .fish-col--b { left: 287px; }
</style>
</head>
<body>

<section class="page page--left">
  <figure class="photo photo--garden" role="img" aria-label="Photo of a house lawn with two white garden chairs, a side table and colourful flower beds">
    <h2 class="photo__title">COMMERCIAL &amp; RESIDENTIAL<br>LANDSCAPING</h2>
  </figure>

  <div class="abs body-text intro">
    <p>In order to ensure the exterior of buildings and homes are kept beautiful and free of fire hazards, it is important to have the proper equipment, training, and knowledge. Meridian Pathways Enterprises can provide equipment and training which will prove to be extremely useful in daily life.</p>
    <p>Some of the equipment to be utilized and potentially purchased is as follows:</p>
  </div>

  <div class="abs equipment-list equipment-list--a body-text">
    <div class="equipment-item">
      <h3 class="equipment-item__name">Weed-Whacker</h3>
      <p>A tool which uses a flexible monofilament line instead of a blade for cutting grass and other plants which are near objects or hard to reach places including steep or irregular terrain. It typically has a long shaft with a handle and a cutting head at the end of the shaft.</p>
    </div>
    <div class="equipment-item">
      <h3 class="equipment-item__name">Lawn Mower</h3>
      <p>Used to trim grass and can be a hand-pushed object or a ride on style.</p>
    </div>
    <div class="equipment-item">
      <h3 class="equipment-item__name">Brush Cutter</h3>
      <p>A heavy duty tool that can clear saplings or dense under growth with ease.</p>
    </div>
  </div>

  <div class="abs equipment-list equipment-list--b body-text">
    <div class="equipment-item">
      <h3 class="equipment-item__name">Chainsaw</h3>
      <p>A handheld, gas powered saw which has the power to cut large trees.</p>
    </div>
    <div class="equipment-item">
      <h3 class="equipment-item__name">Blower</h3>
      <p>A tool which blows air with extreme force in order to push debris from one area to another.</p>
    </div>
    <div class="equipment-item">
      <h3 class="equipment-item__name">Hedge Trimmer</h3>
      <p>Either electric or gas powered versions exist, and are used to efficiently trim bushes and hedges for a manicured look.</p>
    </div>
  </div>

  <footer class="folio folio--left">
    <span>10</span><span class="folio__rule"></span>
    <span class="folio__label"><b>MERIDIAN PATHWAYS ENTERPRISES</b> TRAINING PROGRAM OUTLINE</span>
  </footer>
</section>

<section class="page page--right">
  <div class="tab tab--orange tab--skills">Other Skills</div>

  <div class="skill skill--sprinklers body-text">
    <h3 class="skill__title">SPRINKLERS</h3>
    <p>Learn how to dig proper ditches for efficient drainage, lay sprinkler pipes, and sprinkler head placement for most effective water coverage. Also understand electric control panels and how to program and operate.</p>
  </div>

  <div class="skill skill--design body-text">
    <h3 class="skill__title">DESIGN TECHNIQUES</h3>
    <p>Learn how to beautify grounds through design and strategic placement of specific plants and hardscape items.</p>
  </div>

  <div class="tab tab--equipment">EQUIPMENT</div>
  <p class="abs body-text equipment-note">This training will provide participants with a weedwhacker and a blower so that they may have the tools to start a business right away upon completion of the training.</p>

  <aside class="info-panel">
    <h3 class="info-panel__title">Training Time and Cost</h3>
    <p class="info-panel__text body-text">Training program can be customized for 3 days. Cost: $2100 per person. Minimum class size of 20 required. Classes to be provided in Nairobi, Kenya.</p>
    <div class="tab tab--orange tab--dates">Class Dates (2015)</div>
    <div class="info-bar info-bar--dates">May 20-30</div>
    <div class="tab tab--orange tab--deposit">Final Registration and<br>Deposit Due</div>
    <div class="info-bar info-bar--deposit">December 31, 2015</div>
  </aside>

  <figure class="photo photo--fish" role="img" aria-label="Photo of red snapper and dark fish laid out on crushed ice">
    <h2 class="photo__title">COMMERCIAL FISH FARMING</h2>
  </figure>

  <p class="abs body-text fish-col fish-col--a">Commercial fish farming can be accomplished on a large scale inside of specialized enclosures which can be installed in any location in the world. The term “aquaculture” is used to describe the process by which fish are grown and harvested in these farms. The result is a business that provides a much needed commodity, jobs for local residents, and profits for the business owner.</p>
  <p class="abs body-text fish-col fish-col--b">Meridian Pathways Enterprises provides access to the technology and equipment as well as training for potential business operators and employees. This ensures that individuals have the knowledge and experience required to successfully run the aquaculture farm on a daily basis.</p>

  <footer class="folio folio--right">
    <span class="folio__rule"></span><span>11</span>
  </footer>
</section>

</body>
</html>
```